Catering Menu Package

I currently have a complete menu package, which we have redesigned as far as content, now I need to it put together in a catalog type format. It is essentially 10-12 pages in length, and will be sent for print production. Upon receiving a final edit
Updates

I have added an example gif to the project.

I did this free hand this basically what I am looking for. please change text and type to whatever you think would look best. This is a total rough design so, feel free to change any and everything. The text for the page is on the word documents. If you need more images let me know I am in the process of getting as many images uploaded for your use.

Reason: I figured we got a late jump with questions, so i am extending a few days .

Target Market(s)

The target market is business who wish to have catered luncheons, breakfasts , meetings

Industry/Entity Type

Catering

Requirements
Must have
• I have attached a copy of the text that what we want in the package, our logo, and i have also attached a catering package of another company to give you an idea what the finished product will be
Should not have
• It should not look identical to the example catering packages, these are for some inspiration we want our own design with the same type of look and feel

```html
<!DOCTYPE html>
<html lang="en">
<head>
<meta charset="utf-8">
<title>Light Breakfast — Harborfield Table Caterers</title>
<link rel="stylesheet" href="https://fonts.googleapis.com/css2?family=Lilita+One&family=Norican&family=Tinos:ital,wght@0,400;0,700;1,700&display=swap">
<style>
  :root {
    --parchment-light: #efe3c8;
    --parchment: #e2d2b0;
    --parchment-dark: #c9b48c;
    --ink: #1e1a16;
    --accent: #d6643f;
    --accent-deep: #c4532f;
    --photo-salmon: #d9714a;
    --photo-cream: #efe6d6;
    --photo-crust: #9a5a2c;
  }
  * { margin: 0; padding: 0; box-sizing: border-box; }
  html, body { width: 1200px; height: 927px; overflow: hidden; }
  body { background: var(--parchment); }
  .menu-page {
    position: relative;
    width: 1200px;
    height: 927px;
    overflow: hidden;
    background:
      radial-gradient(ellipse at 35% 40%, var(--parchment-light) 0%, rgba(239,227,200,0) 60%),
      radial-gradient(ellipse at 50% 50%, rgba(0,0,0,0) 55%, rgba(150,120,80,0.35) 100%),
      linear-gradient(160deg, var(--parchment-light), var(--parchment) 55%, var(--parchment-dark));
    color: var(--ink);
  }
  .page-title {
    position: absolute;
    left: 74px;
    top: 52px;
    font-family: "Norican", cursive;
    font-weight: 400;
    font-size: 92px;
    line-height: 1;
    color: var(--accent);
    letter-spacing: -1px;
  }
  .menu-list { position: absolute; left: 76px; top: 0; width: 640px; }
  .menu-item { position: absolute; left: 0; width: 640px; }
  .item-name {
    font-family: "Lilita One", sans-serif;
    font-weight: 400;
    font-size: 23px;
    line-height: 26px;
    letter-spacing: 0.5px;
    color: var(--ink);
  }
  .item-desc {
    margin-top: 1px;
    font-family: "Tinos", serif;
    font-size: 16px;
    line-height: 22.5px;
    color: var(--ink);
  }
  .item-price {
    margin-top: 10px;
    font-family: "Tinos", serif;
    font-weight: 700;
    font-size: 15px;
    text-decoration: line-through;
  }
  .item-quick { top: 218px; }
  .item-fast { top: 312px; }
  .item-lean { top: 428px; }
  .item-newyorker { top: 500px; }
  .item-city { top: 645px; }
  .terms {
    position: absolute;
    left: 76px;
    top: 804px;
    font-family: "Tinos", serif;
    font-style: italic;
    font-weight: 700;
    font-size: 15.5px;
    line-height: 21px;
  }
  .brand {
    position: absolute;
    left: 975px;
    top: 90px;
    width: 170px;
    text-align: center;
    font-family: "Lilita One", sans-serif;
    font-size: 27px;
    line-height: 32px;
    color: var(--ink);
  }
  .brand-mark {
    display: block;
    width: 44px;
    height: 44px;
    margin: 0 auto 18px;
    background: var(--accent);
  }
  .footer-band {
    position: absolute;
    left: 0;
    bottom: 0;
    width: 1200px;
    height: 52px;
    background: var(--accent-deep);
  }
  .footer-band::before {
    content: "";
    position: absolute;
    left: 0; right: 0; top: -4px;
    height: 2px;
    background: var(--parchment-light);
  }
  .feature-photo { position: absolute; left: 790px; top: 440px; }
</style>
</head>
<body>
<main class="menu-page">
  <h1 class="page-title">Light Breakfast</h1>

  <div class="brand">
    <span class="brand-mark"></span>
    Harborfield<br>Table<br>Caterers
  </div>

  <section class="menu-list">
    <article class="menu-item item-quick">
      <h2 class="item-name">Quick and Easy</h2>
      <p class="item-desc">French Pastry, a Fresh Baked Gourmet Muffin,and Whole Fresh Fruit(Featuring<br>Local Apples and Peaches, California Oranges, or Bananas).</p>
    </article>
    <article class="menu-item item-fast">
      <h2 class="item-name">Fast Farmhouse</h2>
      <p class="item-desc">Fresh baked Breakfast Bread and Buttery Biscuits, Whipped Butter and House-<br>made Strawberry Jam and Local Fruit Jellies, and Whole Fresh Fruit(Featuring<br>Local Apples and Peaches, California Oranges, or Bananas).</p>
    </article>
    <article class="menu-item item-lean">
      <h2 class="item-name">Light and Lean</h2>
      <p class="item-desc">Individual Yogurt, Fresh Fruit and Berry Cups and House-made Granola.</p>
    </article>
    <article class="menu-item item-newyorker">
      <h2 class="item-name">New Yorker</h2>
      <p class="item-desc">Brooklyn Bagel, Whipped Cream Cheese, House-made Strawberry Jam and<br>Local Fruit Jellies, Whipped Butter, and Whole Fresh Fruit(Featuring Local<br>Apples and Peaches, California Oranges, or Bananas). Add Smoked Salmon</p>
      <p class="item-price">$6.66</p>
    </article>
    <article class="menu-item item-city">
      <h2 class="item-name">City Farmhouse</h2>
      <p class="item-desc">Fresh Baked Buttery Biscuits, Gourmet Muffins and Breakfast Breads, Brooklyn<br>Bagels, Whole Fresh Fruit(Featuring Local Apples and Peaches, California<br>Oranges, or Bananas), Whipped Butter and Cream Cheese, House-made<br>Strawberry Jam and Local Fruit Jellies.</p>
    </article>
  </section>

  <p class="terms">All Prices are per Person, with a 10 person minimum order per item chosen.<br>Local Products used when available and in season</p>

  <div class="footer-band"></div>

  <svg class="feature-photo" width="520" height="520" viewBox="0 0 520 520" role="img" aria-label="Photo of a toasted bagel topped with cream cheese, smoked salmon and chopped chives">
    <defs>
      <radialGradient id="photoTone" cx="45%" cy="45%" r="60%">
        <stop offset="0%" stop-color="var(--photo-salmon)"/>
        <stop offset="55%" stop-color="#c8663f"/>
        <stop offset="80%" stop-color="var(--photo-crust)"/>
        <stop offset="100%" stop-color="var(--photo-cream)"/>
      </radialGradient>
    </defs>
    <circle cx="260" cy="260" r="250" fill="url(#photoTone)"/>
    <circle cx="260" cy="260" r="254" fill="none" stroke="var(--ink)" stroke-width="2" stroke-dasharray="3 3"/>
  </svg>
</main>
</body>
</html>
```